Most captivating card ever!

Life Coach - Professional Adventurer - Entrepreneur
I need the worlds most amazing business card for my personal brand. This business card will mostly be used to give to prospective clients for life coaching and business coaching.
Be creative, be adventurous. It needs to stand out. Make people say.. I need this guy!
My background is as an entrepreneur and professional adventurer undertaking extreme expeditions. I am now moving into life coaching.
No specific design ideas, so you have full creativity. Show me your best.
Industry/Entity Type
Life Coaching
Contact Information for Business Card
Dan Pellow
itsdanp.com.au
0468215903
Colors
Designer to choose colors to be used in the design.
Look and feel

```html
<!DOCTYPE html>
<html lang="en">
<head>
<meta charset="utf-8">
<title>Dan Pellow — Business Card</title>
<link rel="stylesheet" href="https://fonts.googleapis.com/css2?family=Oswald:wght@600&family=Saira+Condensed:wght@400;600&family=Titillium+Web:wght@400&display=swap">
<style>
  :root {
    --backdrop: #0f0f0f;
    --card: #252525;
    --card-edge: #2e2e2e;
    --ink-white: #ffffff;
    --ink-orange: #f27a21;
    --bar-text: #1c1c1c;
  }
  html, body {
    margin: 0;
    width: 1200px;
    height: 1000px;
    overflow: hidden;
    background: var(--backdrop);
  }
  .card {
    position: absolute;
    left: 180px;
    top: 260px;
    width: 840px;
    height: 480px;
    border-radius: 22px;
    background: linear-gradient(160deg, var(--card-edge) 0%, var(--card) 55%, #1f1f1f 100%);
    box-shadow: 0 20px 50px rgba(0,0,0,0.6);
    overflow: hidden;
  }
  .name {
    position: absolute;
    left: 62px;
    top: 40px;
    margin: 0;
    font-family: "Oswald", sans-serif;
    font-weight: 600;
    font-size: 104px;
    line-height: 0.92;
    letter-spacing: 2px;
    text-transform: uppercase;
  }
  .name__first { display: block; color: var(--ink-white); }
  .name__last { display: block; color: var(--ink-orange); }
  .tagline {
    position: absolute;
    left: 50px;
    top: 262px;
    width: 660px;
    height: 44px;
    background: var(--ink-white);
    box-sizing: border-box;
    padding-left: 16px;
    font-family: "Titillium Web", sans-serif;
    font-size: 25px;
    line-height: 44px;
    color: var(--bar-text);
    white-space: nowrap;
  }
  .contact {
    position: absolute;
    left: 50px;
    top: 318px;
    font-family: "Saira Condensed", sans-serif;
    font-size: 60px;
    line-height: 1;
    white-space: nowrap;
    letter-spacing: 1px;
  }
  .contact__phone { color: var(--ink-orange); font-weight: 400; }
  .contact__sep { color: var(--ink-white); margin: 0 14px; }
  .contact__web { font-weight: 600; text-transform: uppercase; }
  .web--white { color: var(--ink-white); }
  .web--orange { color: var(--ink-orange); }
</style>
</head>
<body>
  <div class="card">
    <h1 class="name">
      <span class="name__first">Dan</span>
      <span class="name__last">Pellow</span>
    </h1>
    <div class="tagline">Life Coach - Professional Adventurer - Entrepreneur</div>
    <div class="contact">
      <span class="contact__phone">046 821 5903</span><span class="contact__sep">-</span><span class="contact__web"><span class="web--white">its</span><span class="web--orange">danp</span><span class="web--white">.com.au</span></span>
    </div>
  </div>
</body>
</html>
```